Elegant Candy Buffet & Jar Hire Needs a logo & business card design

I need a logo design and a business card design for a new candy buffet company based in Melbourne called "Maple Candy Buffet & Jar Hire"(but the & Jar Hire part to be in smaller font). We set up candy bars with a wide variety of custom themes or to the customer's preference, we also hire out the glass jars if the customer prefers to do it themselves. But i want the emphasis on the front of the business card to be about the Candy Buffet and the jar hire can be at the back of the card. I would like to see designs that use the tiffany blue, or black and gold. I would like to see elegance, class but quite simple.

Industry/Entity Type

Business

Font styles to use
Script

```html
<!DOCTYPE html>
<html lang="en">
<head>
<meta charset="utf-8">
<title>Maple Candy Buffet &amp; Jar Hire – Business Card</title>
<link rel="stylesheet" href="https://fonts.googleapis.com/css2?family=Arimo&family=Della+Respira&display=swap">
<style>
  :root {
    --page-bg: #ffffff;
    --cream: #f8e8d2;
    --cream-light: #fbf0e0;
    --cream-shade: #efdcc3;
    --frame-dark: #3f8a5e;
    --frame-light: #9fd9a8;
    --gold: #b8902a;
    --green-top: #4e9168;
    --green-mid: #6fa97c;
    --green-bottom: #c6e6b4;
    --ink-green: #4f9a6e;
    --ink-cream: #f6ecd6;
    --ink-faint: #86c39b;
    --shadow: rgba(0, 0, 0, 0.18);
    --font-display: "Della Respira", Georgia, serif;
    --font-sans: "Arimo", Arial, sans-serif;
  }

  * { box-sizing: border-box; margin: 0; padding: 0; }

  html, body {
    width: 1200px;
    height: 900px;
    overflow: hidden;
    background: var(--page-bg);
  }

  .canvas {
    position: relative;
    width: 1200px;
    height: 900px;
    font-family: var(--font-display);
  }

  .card {
    position: absolute;
    top: 285px;
    width: 540px;
    height: 330px;
    border-radius: 24px;
    overflow: hidden;
    box-shadow: 0 14px 28px var(--shadow);
  }

  /* Front */
  .card-front {
    left: 45px;
    background: var(--cream);
  }

  .front-pattern {
    position: absolute;
    inset: 0;
    background: radial-gradient(ellipse at 50% 45%, var(--cream-light) 0%, var(--cream) 55%, var(--cream-shade) 100%);
  }

  .front-frame {
    position: absolute;
    inset: 0;
  }

  .brand-lockup {
    position: absolute;
    left: 0;
    right: 0;
    top: 92px;
    text-align: center;
    font-weight: 400;
  }

  .brand-name {
    display: block;
    font-family: var(--font-display);
    font-size: 84px;
    line-height: 1;
    letter-spacing: 1px;
    color: var(--gold);
  }

  .brand-tagline {
    display: block;
    margin-top: 14px;
    font-family: var(--font-sans);
    font-size: 19px;
    color: var(--ink-green);
  }

  /* Back */
  .card-back {
    left: 615px;
    background: linear-gradient(180deg, var(--green-top) 0%, var(--green-mid) 45%, var(--green-bottom) 100%);
    text-align: center;
  }

  .back-brand {
    position: absolute;
    left: 0;
    right: 0;
    top: 36px;
    color: var(--ink-faint);
    font-weight: 400;
  }

  .back-brand-name {
    display: block;
    font-size: 44px;
    line-height: 1;
  }

  .back-brand-tagline {
    display: block;
    margin-top: 6px;
    font-family: var(--font-sans);
    font-size: 10px;
  }

  .back-message {
    position: absolute;
    left: 0;
    right: 0;
    top: 140px;
    color: var(--ink-cream);
  }

  .message-lead {
    font-size: 22px;
    letter-spacing: 0.3px;
  }

  .message-sub {
    margin-top: 4px;
    font-size: 20px;
    opacity: 0.9;
  }

  .contact-line {
    margin-top: 22px;
    font-size: 15px;
    letter-spacing: 0.3px;
  }
</style>
</head>
<body>
<main class="canvas">

  <section class="card card-front">
    <div class="front-pattern" role="img" aria-label="Soft cream damask floral pattern covering the card face"></div>
    <svg class="front-frame" width="540" height="330" viewBox="0 0 540 330" aria-hidden="true">
      <defs>
        <linearGradient id="frameGradient" x1="0" y1="0" x2="1" y2="1">
          <stop offset="0" stop-color="#3f8a5e"/>
          <stop offset="0.45" stop-color="#9fd9a8"/>
          <stop offset="0.7" stop-color="#3f8a5e"/>
          <stop offset="1" stop-color="#9fd9a8"/>
        </linearGradient>
      </defs>
      <rect x="13" y="13" width="514" height="304" rx="16" ry="16" fill="none" stroke="url(#frameGradient)" stroke-width="7"/>
    </svg>
    <h1 class="brand-lockup">
      <span class="brand-name">Maple</span>
      <span class="brand-tagline">Candy Buffet &amp; Jar Hire</span>
    </h1>
  </section>

  <section class="card card-back">
    <div class="back-brand">
      <span class="back-brand-name">Maple</span>
      <span class="back-brand-tagline">Candy Buffet &amp; Jar Hire</span>
    </div>
    <div class="back-message">
      <p class="message-lead">Enjoy in some sweet decadance</p>
      <p class="message-sub">at your next special event</p>
      <p class="contact-line">Please Contact Clara on 0400 555 019</p>
    </div>
  </section>

</main>
</body>
</html>
```